Interior Plaster, Plasterboard Fixing & Installation Business CardDesign

GLAZEON The name was formed by me, in talking to my accountant, whilst skim coating his walls and I had seen an imperfection in a wall that needed to be skim coated to deflect the light from the imperfection. I responded to him saying...."just Glaze On". The idea originates from the process of applying a skim coat of interior plaster to a wall to achieve a smoother surface. This is required prior to many applications, applying wall paper, preparation for paint, after removing wall paper, improving aesthetics, joints that have not been properly jointed etc. Different types of light reflected on the surface, makes poor jointing more visible. In addition, the businesses key functions will be interior plastering, plaster board installation (ceilings and walls) and plasterboard jointing to a level that is prepared for a painter. Once the plaster is applied the surface requires sanding using different types of sanding equipment manual and electronic, including the use of specialised paint-on sealers for the surface. I believe the name is simple, easy to remember, but may be read incorrectly. I have had people ask if it was Glaze On, referring to information technology.

For now, this entire concept is driven by passion and started 2 years ago whilst renovating my own home.

I need to be able to use your expertise to translate my ideas, starting with business card and progressing to a website incorporating anything and everything in between. The final design should be easy to understand, read and standout with an element of uniqueness. Humour maybe an option, or the idea of leaving a prospect with something that is thought provoking.
Updates

Hi All Ideas look fine so far, but would expect to see different colour options. I am thinking plaster thats cream in colour, so more earthy colour on the card. A picture of a trowel to replace the I in GLAZEON maybe. I like the swirl that is created by a notched trowel moving through plaster. Perhaps a more modern or fresher look. With GLAZEON, could you consider reversing the direction of the K for instance facing in the opposite direction. In saying this I look to you for your experience and expertise with the idea. The other option with the K, could be to remove the first straight line, i hope that my explanation helps. Sorry if it doesn't. Thanks heaps :)

Please include the type of service. Plasterboard Services

I have considered the idea of the K being reversed, and I am of the view that it presents a challenge reading and understanding. Moving forward I would however like to use the K in the normal direction but without the first straight line. I need to see more colour options that are grey or earthy. Can a picture of a trowel be included if it makes sense and with that tool being frequently used in plastering.

Industry/Entity Type

Business

Contact Information for Business Card

Company name: GlazeOn
Name: Dorian Pevey
Title: Director
Email address: peveydr@mailbox-example.net
Mobile number: 0210 481 7294
Address: 17 Tamsin Lane, Glenfield, Auckland, 0629

```html
<!DOCTYPE html>
<html lang="en">
<head>
<meta charset="utf-8">
<title>GlazeOn Business Card</title>
<link href="https://fonts.googleapis.com/css2?family=Oswald:wght@400;600;700&family=Exo+2:wght@400;500&display=swap" rel="stylesheet">
<style>
  :root {
    --charcoal: #3a3a3b;
    --charcoal-deep: #333334;
    --orange: #ea6a24;
    --white: #ffffff;
    --ink: #2f2f30;
    --backdrop: #e9e6e1;
  }
  * { margin: 0; padding: 0; box-sizing: border-box; }
  html, body { width: 1200px; height: 1019px; overflow: hidden; }
  body {
    background: var(--backdrop);
    display: flex;
    flex-direction: column;
    align-items: center;
    justify-content: center;
    gap: 70px;
  }
  .card {
    width: 760px;
    height: 434px;
    position: relative;
    overflow: hidden;
    box-shadow: 0 10px 28px rgba(0,0,0,0.22);
  }

  /* Front */
  .card-front { display: flex; background: var(--charcoal); }
  .identity-side {
    width: 50%;
    background: var(--charcoal);
    padding: 86px 0 86px 42px;
  }
  .identity-panel {
    height: 100%;
    background: var(--white);
    display: flex;
    flex-direction: column;
    justify-content: center;
    padding-left: 36px;
  }
  .brand-name {
    font-family: "Oswald", sans-serif;
    font-weight: 700;
    font-size: 62px;
    color: var(--orange);
    line-height: 1;
    letter-spacing: 0.5px;
  }
  .person { margin-top: 26px; align-self: flex-end; padding-right: 22px; }
  .person-name {
    font-family: "Oswald", sans-serif;
    font-weight: 600;
    font-size: 27px;
    color: var(--ink);
    text-transform: uppercase;
    letter-spacing: 0.5px;
    line-height: 1.1;
  }
  .person-title {
    font-family: "Exo 2", sans-serif;
    font-size: 17px;
    color: var(--ink);
  }
  .contact-side {
    width: 50%;
    background: var(--orange);
    padding: 86px 42px 86px 0;
  }
  .contact-panel {
    height: 100%;
    background: var(--charcoal-deep);
    padding: 30px 24px 0 22px;
    list-style: none;
    font-family: "Exo 2", sans-serif;
    font-size: 14px;
    color: var(--white);
  }
  .contact-item {
    display: flex;
    align-items: flex-start;
    gap: 10px;
    margin-bottom: 11px;
    line-height: 1.3;
  }
  .contact-icon { width: 13px; height: 13px; flex: none; margin-top: 2px; fill: var(--white); }

  /* Back */
  .card-back { background: var(--charcoal); padding: 40px; }
  .back-panel { width: 100%; height: 100%; display: block; }
</style>
</head>
<body>

<section class="card card-front" aria-label="Business card front">
  <div class="identity-side">
    <div class="identity-panel">
      <div class="brand-name">GlazeOn</div>
      <div class="person">
        <div class="person-name">Dorian Pevey</div>
        <div class="person-title">Director</div>
      </div>
    </div>
  </div>
  <div class="contact-side">
    <ul class="contact-panel">
      <li class="contact-item">
        <svg class="contact-icon" viewBox="0 0 12 12"><path d="M6 0a4 4 0 0 0-4 4c0 3 4 8 4 8s4-5 4-8a4 4 0 0 0-4-4zm0 5.5A1.5 1.5 0 1 1 6 2.5a1.5 1.5 0 0 1 0 3z"/></svg>
        <span>17 Tamsin Lane, Glenfield,<br>Auckland, 0629</span>
      </li>
      <li class="contact-item">
        <svg class="contact-icon" viewBox="0 0 12 12"><path d="M2.5 0.5l2 2.2-1 1.3c.8 1.6 2 2.8 3.5 3.5l1.3-1 2.2 2-1.3 2.2C5 10.5 1.5 7 .3 1.8z"/></svg>
        <span>0210 481 7294</span>
      </li>
      <li class="contact-item">
        <svg class="contact-icon" viewBox="0 0 12 12"><path d="M3 0h6v12H3zM4 1.5v8h4v-8z"/></svg>
        <span>0210 481 7294</span>
      </li>
      <li class="contact-item">
        <svg class="contact-icon" viewBox="0 0 12 12"><path d="M0 2h12v8H0zM1.2 3.2L6 6.6l4.8-3.4V3H1.2z"/></svg>
        <span>peveydr@mailbox-example.net</span>
      </li>
      <li class="contact-item">
        <svg class="contact-icon" viewBox="0 0 12 12"><path d="M6 0a6 6 0 1 0 0 12A6 6 0 0 0 6 0zm0 1.2c.8.9 1.3 2.4 1.4 4.2H4.6C4.7 3.6 5.2 2.1 6 1.2zM1.2 6.6h2.2c.1 1.6.5 3 1.2 4A4.8 4.8 0 0 1 1.2 6.6zm0-1.2a4.8 4.8 0 0 1 3.4-4c-.7 1-1.1 2.4-1.2 4zm4.8 5.4c-.8-.9-1.3-2.4-1.4-4.2h2.8c-.1 1.8-.6 3.3-1.4 4.2zm1.4-.2c.7-1 1.1-2.4 1.2-4h2.2a4.8 4.8 0 0 1-3.4 4zm1.2-5.2c-.1-1.6-.5-3-1.2-4a4.8 4.8 0 0 1 3.4 4z"/></svg>
        <span>www.glazeon-example.net</span>
      </li>
    </ul>
  </div>
</section>

<section class="card card-back" aria-label="Business card back">
  <svg class="back-panel" viewBox="0 0 680 354" preserveAspectRatio="none" aria-hidden="true">
    <polygon points="0,0 680,0 0,354" fill="var(--orange)"/>
    <polygon points="680,0 680,354 0,354" fill="var(--white)"/>
  </svg>
</section>

</body>
</html>
```